Creative & Appealing Business Card

Required a business card for Vantrelink
We specialise in claims management services for PPI ( Payment Protection Insurance.
2 sided business card
Round Corners
I like embossed and raised lettering

```html
<!DOCTYPE html>
<html lang="en">
<head>
<meta charset="utf-8">
<title>Vantrelink Business Card</title>
<link rel="stylesheet" href="https://fonts.googleapis.com/css2?family=Arimo:wght@400;700&display=swap">
<style>
  :root {
    --stage: #2c2e30;
    --card-light: #4a6670;
    --card-dark: #2f4a54;
    --ink: #ffffff;
    --ink-soft: #dbe6ea;
    --emboss-hi: rgba(255,255,255,0.16);
    --emboss-lo: rgba(0,0,0,0.28);
  }
  * { margin: 0; padding: 0; box-sizing: border-box; }
  html, body { width: 1200px; height: 1000px; overflow: hidden; }
  body {
    background: var(--stage);
    font-family: "Arimo", Arial, sans-serif;
    color: var(--ink);
    display: flex;
    flex-direction: column;
    align-items: center;
    justify-content: center;
    gap: 56px;
  }
  .card {
    position: relative;
    width: 700px;
    height: 400px;
    border-radius: 26px;
    background: linear-gradient(160deg, var(--card-light) 0%, var(--card-dark) 100%);
    box-shadow: 0 14px 30px rgba(0,0,0,0.45);
    overflow: hidden;
  }

  /* Logo side */
  .card--brand {
    display: flex;
    flex-direction: column;
    align-items: center;
    justify-content: center;
    text-align: center;
  }
  .brand-mark {
    width: 96px; height: 96px;
    border-radius: 50%;
    background: var(--ink);
    margin-bottom: 26px;
  }
  .brand-name {
    font-weight: 700;
    font-size: 60px;
    letter-spacing: -0.5px;
    line-height: 1;
  }
  .brand-tagline {
    margin-top: 10px;
    font-size: 17px;
    letter-spacing: 1.5px;
    text-transform: uppercase;
    color: var(--ink-soft);
  }
  .brand-services {
    margin-top: 14px;
    font-weight: 700;
    font-size: 21px;
    line-height: 1.3;
  }

  /* Contact side */
  .card--contact { padding: 44px 48px; }
  .contact-brand {
    display: flex;
    align-items: center;
    gap: 14px;
  }
  .contact-brand .dot {
    width: 46px; height: 46px;
    border-radius: 50%;
    background: var(--ink);
  }
  .contact-brand .name {
    font-weight: 700;
    font-size: 34px;
    letter-spacing: -0.3px;
  }
  .person {
    margin-top: 40px;
    font-size: 26px;
    text-transform: uppercase;
    letter-spacing: 0.5px;
  }
  .person strong { font-weight: 700; }
  .contact-list {
    list-style: none;
    margin-top: 12px;
    font-size: 17px;
    line-height: 1.4;
    color: var(--ink-soft);
  }
  .contact-list li { display: flex; align-items: center; gap: 10px; }
  .contact-list svg { width: 16px; height: 16px; fill: var(--ink); flex: none; }
  .address {
    margin-top: 12px;
    font-size: 17px;
    line-height: 1.3;
    color: var(--ink-soft);
    font-style: normal;
    padding-left: 26px;
  }
  .address strong { color: var(--ink); }
  .emboss-disc {
    position: absolute;
    right: 60px;
    top: 60px;
    width: 250px; height: 250px;
    border-radius: 50%;
    background: linear-gradient(150deg, rgba(255,255,255,0.07), rgba(0,0,0,0.06));
    box-shadow:
      -3px -3px 6px var(--emboss-hi),
      4px 5px 9px var(--emboss-lo),
      inset 2px 2px 3px var(--emboss-hi),
      inset -2px -2px 4px var(--emboss-lo);
  }
</style>
</head>
<body>

  <section class="card card--brand" aria-label="Card front">
    <div class="brand-mark"></div>
    <h1 class="brand-name">Vantrelink</h1>
    <p class="brand-tagline">Claims Management Services</p>
    <p class="brand-services">Payment Protection Insurance<br>Interest Rate Swaps</p>
  </section>

  <section class="card card--contact" aria-label="Card back">
    <div class="emboss-disc"></div>
    <div class="contact-brand">
      <span class="dot"></span>
      <span class="name">Vantrelink</span>
    </div>
    <h2 class="person"><strong>Tariq</strong> Malden</h2>
    <ul class="contact-list">
      <li>
        <svg viewBox="0 0 16 16"><path d="M3.5 1l2.5 0 1 3.5-1.6 1.2a8 8 0 0 0 4.9 4.9l1.2-1.6 3.5 1v2.5c0 .8-.7 1.5-1.5 1.5A13 13 0 0 1 2 2.5C2 1.7 2.7 1 3.5 1z"/></svg>
        +44 (0) 300 555 0142
      </li>
      <li>
        <svg viewBox="0 0 16 16"><path d="M4 1h7l2 2v3H4zM2 7h12a1 1 0 0 1 1 1v5a1 1 0 0 1-1 1H2a1 1 0 0 1-1-1V8a1 1 0 0 1 1-1zm2 2v1h3V9zm0 2v1h3v-1z"/></svg>
        +44 (0) 208 555 0187
      </li>
      <li>
        <svg viewBox="0 0 16 16"><path d="M1 3h14v10H1zm1.5 1.2v.5L8 9l5.5-4.3v-.5zM2.5 6.4V12h11V6.4L8 10.7z"/></svg>
        tariq@vantrelink.com
      </li>
      <li>
        <svg viewBox="0 0 16 16"><path d="M8 1a7 7 0 1 0 0 14A7 7 0 0 0 8 1zm0 1.5c.8 0 1.7 1.6 2 4H6c.3-2.4 1.2-4 2-4zm-2 5.5h4c-.2 2.6-1.1 5.5-2 5.5s-1.8-2.9-2-5.5zM2.6 7h2c0-1.6.4-3 .9-4a5.5 5.5 0 0 0-2.9 4zm0 1.5a5.5 5.5 0 0 0 2.9 4.1 10 10 0 0 1-.9-4.1zm10.8 0h-2a10 10 0 0 1-.9 4.1 5.5 5.5 0 0 0 2.9-4.1zm0-1.5a5.5 5.5 0 0 0-2.9-4c.5 1 .9 2.4.9 4z"/></svg>
        www.vantrelink.com
      </li>
    </ul>
    <address class="address">
      <strong>Vantrelink</strong><br>
      48 Ashgrove Lane<br>
      London N4 2PL
    </address>
  </section>

</body>
</html>
```